Looking to update current business card

We have a two sided card currently that needs a fresher, newer look. I like the fact it has two sides with a list of products/services we offer on the back side but the overall front look is lackluster. Our logo will stay the same.. I just want someone to bring some new life into the business card.

I like cards that have rounded corners but not sure if there's enough room?

Attached is our current biz card design and logo.

Target Market(s)

business customers

Industry/Entity Type

Business

Contact Information for Business Card

see above

```html
<!DOCTYPE html>
<html lang="en">
<head>
<meta charset="utf-8">
<title>Harborline Data Group – Business Card</title>
<link rel="stylesheet" href="https://fonts.googleapis.com/css2?family=Arimo:wght@400;700&display=swap">
<style>
  :root {
    --stage: #ece9e4;
    --card-top: #f4f5f6;
    --card-bottom: #dfe1e3;
    --brand-blue: #1f4fa8;
    --brand-orange: #f07a1f;
    --muted-grey: #a9adb2;
  }
  * { margin: 0; padding: 0; box-sizing: border-box; }
  html, body { width: 1200px; height: 1000px; overflow: hidden; }
  body {
    background: var(--stage);
    font-family: "Arimo", Arial, sans-serif;
    position: relative;
  }
  .business-card {
    position: absolute;
    left: 180px; top: 260px;
    width: 840px; height: 480px;
    border-radius: 44px;
    background: linear-gradient(160deg, var(--card-top), var(--card-bottom));
    box-shadow: 0 6px 18px rgba(0,0,0,.15);
    overflow: hidden;
  }
  .corner-pattern {
    position: absolute; left: 0; top: 0;
    width: 300px; height: 300px;
  }
  .company-heading {
    position: absolute;
    left: 330px; top: 40px;
    font-size: 25px;
    font-weight: 700;
    color: var(--brand-blue);
    padding-bottom: 6px;
    border-bottom: 4px solid var(--brand-orange);
    white-space: nowrap;
  }
  .brand-name {
    position: absolute;
    left: 300px; top: 112px;
    display: flex; align-items: center; gap: 14px;
  }
  .brand-name .wordmark {
    font-size: 46px; line-height: 1;
    font-weight: 400;
    color: var(--brand-blue);
    white-space: nowrap;
  }
  .brand-name .dot {
    width: 20px; height: 20px; border-radius: 50%;
    background: var(--brand-orange);
  }
  .brand-web {
    position: absolute; left: 304px; top: 196px;
    font-size: 22px; color: var(--muted-grey);
  }
  .contact-details {
    position: absolute; left: 250px; top: 244px;
    width: 420px; text-align: center;
    color: var(--brand-blue);
    font-size: 23px; line-height: 29px;
    font-style: normal;
  }
  .office-address {
    position: absolute; left: 0; right: 0; top: 410px;
    text-align: center; font-size: 22px;
    color: var(--brand-blue);
  }
</style>
</head>
<body>
  <article class="business-card">
    <svg class="corner-pattern" viewBox="0 0 300 300" role="img" aria-label="Decorative diagonal band of repeated company lettering in soft orange">
      <defs>
        <linearGradient id="bandTone" x1="0" y1="0" x2="1" y2="1">
          <stop offset="0" stop-color="#f8d6bf"/>
          <stop offset="1" stop-color="#fbe6d8"/>
        </linearGradient>
      </defs>
      <polygon points="0,0 250,0 0,250" fill="url(#bandTone)"/>
    </svg>

    <h1 class="company-heading">Harborline Data Group, Inc</h1>

    <div class="brand-name">
      <span class="wordmark">Harborline Data</span>
      <span class="dot"></span>
    </div>
    <p class="brand-web">www.harborlinegrp.com</p>

    <address class="contact-details">
      <p class="person-name">Daniel Moreau</p>
      <p>E:Dmoreau@harborlinegrp.com</p>
      <p>D:617.555.0142</p>
      <p>F:866.555.0178</p>
    </address>

    <p class="office-address">18 Linden Street Riverton, MA 02140</p>
  </article>
</body>
</html>
```